Salve Label

2.25 inch round label.

We are looking for a simple label, muted natural colors, sophisticated, elegant, calming.

Name of Product: Herbal Beeswax Salve
This scent is lavender - but there will be others scents
Want this label to be adaptable to other scents with simple color and word changes.

Other things to express on the label - all natural, calming, relaxing

Name of the Company: Tansy Ridge Farm
2 oz.

```html
<!DOCTYPE html>
<html lang="en">
<head>
<meta charset="UTF-8">
<title>Herbal Beeswax Salve – Round Labels</title>
<link rel="stylesheet" href="https://fonts.googleapis.com/css2?family=Open+Sans:wght@700&family=Great+Vibes&family=Source+Sans+3:ital,wght@1,300;1,400&display=swap">
<style>
  :root {
    --page: #ffffff;
    --ink: #0d0d0d;
    --silver-light: #f1f1f1;
    --silver-mid: #cfcfcf;
    --silver-dark: #a9a9a9;
    --lavender: #7c2b8f;
    --loosestrife: #b53c98;
    --scent-text: #d9cfe0;
    --plant-area: #c6c6c6;
    --note: #222222;
  }
  html, body {
    margin: 0;
    padding: 0;
    width: 1200px;
    height: 625px;
    overflow: hidden;
    background: var(--page);
  }
  .label-sheet { display: block; width: 1200px; height: 625px; }
  .label-title {
    font-family: "Open Sans", sans-serif;
    font-weight: 700;
    fill: var(--ink);
    text-anchor: middle;
  }
  .label-title--small { font-size: 41px; }
  .label-title--large { font-size: 47px; }
  .label-size {
    font-family: "Open Sans", sans-serif;
    font-weight: 700;
    font-size: 38px;
    fill: var(--ink);
    text-anchor: middle;
  }
  .scent-name {
    font-family: "Great Vibes", cursive;
    font-size: 36px;
    fill: var(--scent-text);
    text-anchor: middle;
  }
  .scent-badge--lavender { fill: var(--lavender); }
  .scent-badge--loosestrife { fill: var(--loosestrife); }
  .plant-art { fill: var(--plant-area); opacity: 0.55; }
  .dimension-note {
    font-family: "Source Sans 3", sans-serif;
    font-style: italic;
    font-weight: 300;
    font-size: 28px;
    fill: var(--note);
    text-anchor: middle;
  }
  .print-note {
    font-family: "Source Sans 3", sans-serif;
    font-style: italic;
    font-weight: 400;
    font-size: 17px;
    fill: var(--note);
  }
  .leader-line { stroke: #555; stroke-width: 0.7; }
</style>
</head>
<body>
<svg class="label-sheet" viewBox="0 0 1200 625" xmlns="http://www.w3.org/2000/svg">
  <defs>
    <radialGradient id="silverFoil" cx="45%" cy="40%" r="65%">
      <stop offset="0%" stop-color="var(--silver-light)"/>
      <stop offset="60%" stop-color="var(--silver-mid)"/>
      <stop offset="100%" stop-color="var(--silver-dark)"/>
    </radialGradient>
  </defs>

  <!-- Lavender label -->
  <g class="label label--lavender">
    <circle class="label-foil" cx="310" cy="300" r="257" fill="url(#silverFoil)"/>
    <text class="label-title label-title--small" x="310" y="151">HERBAL</text>
    <text class="label-title label-title--large" x="310" y="196">Beeswax Salve</text>
    <rect class="plant-art" x="277" y="213" width="76" height="182" rx="10" role="img" aria-label="Line drawing of lavender sprigs"/>
    <ellipse class="scent-badge scent-badge--lavender" cx="302" cy="448" rx="99" ry="34"/>
    <text class="scent-name" x="302" y="460">Lavender</text>
    <text class="label-size" x="315" y="524">2 oz.</text>
  </g>

  <!-- Loosestrife label -->
  <g class="label label--loosestrife">
    <circle class="label-foil" cx="887" cy="300" r="257" fill="url(#silverFoil)"/>
    <text class="label-title label-title--small" x="887" y="151">HERBAL</text>
    <text class="label-title label-title--large" x="887" y="196">Beeswax Salve</text>
    <rect class="plant-art" x="855" y="220" width="50" height="171" rx="10" role="img" aria-label="Line drawing of a loosestrife flower stem"/>
    <ellipse class="scent-badge scent-badge--loosestrife" cx="878" cy="448" rx="99" ry="34"/>
    <text class="scent-name" x="880" y="460">Loosestrife</text>
    <text class="label-size" x="892" y="524">2 oz.</text>
  </g>

  <!-- Production notes -->
  <text class="dimension-note" x="334" y="602">2.25″x2.25″</text>
  <line class="leader-line" x1="566" y1="571" x2="714" y2="490"/>
  <text class="print-note" x="561" y="592">* printing on metalic or silver sticker</text>
</svg>
</body>
</html>
```